Professionelles Design für Use Case Präsentationen im B2B-Bereich

Wir sind ein Schweizer Technologieunternehmen (Kalvor GmbH, www.kalvor.ch), das datenbasierte Simulationen, Optimierung und Entscheidungsunterstützung für Unternehmen in Logistik, Produktion und Verkehr anbietet.
Ziel dieses Projekts ist es, bestehende Use Cases in ein modernes, visuell ansprechendes Format zu bringen, das unsere Kompetenz und den Nutzen für Kunden klar kommuniziert. Die Zielgruppe sind Entscheidungsträger in mittleren bis großen Industrieunternehmen (Bereichsleiter, Projektleiter, Geschäftsleitung).
Was wir brauchen:
– Ein cleanes, professionelles Design (PowerPoint oder PDF-Layout), das sich gut für Präsentationen, Whitepaper oder als LinkedIn-Content eignet.
– Klare Struktur mit Infografiken, Icons, Diagrammen oder Visualisierungen.
– Integration unseres Logos, Farbschemas und ggf. unseres Slogans.
Stilrichtung:
– Modern, technisch fundiert, aber nicht überladen
– Klar, direkt, seriös
– Gerne mit einem visuellen roten Faden (z. B. durchgängige Icons oder Layout-Struktur)
Ein Beispieldokument (UseCase Transportkosten) mit Inhalte ist angefügt. Ziel ist eine wiederverwendbare Vorlage, die wir für verschiedene Kunden-Use-Cases adaptieren können.
- Roboto

```html
<!DOCTYPE html>
<html lang="de">
<head>
<meta charset="utf-8">
<title>Kalvor – Use Case Transportkosten</title>
<link href="https://fonts.googleapis.com/css2?family=Roboto:ital,wght@0,300;0,400;0,500;0,700;1,500&family=Roboto+Condensed:wght@700;800&display=swap" rel="stylesheet">
<style>
  :root{
    --mat:#a7a7a7;
    --forest:#283321;
    --lime:#dde063;
    --paper:#ffffff;
    --ink:#3a3a3a;
  }
  *{margin:0;padding:0;box-sizing:border-box}
  html,body{width:1200px;height:777px;overflow:hidden;background:var(--mat)}
  body{font-family:"Roboto",sans-serif;position:relative}
  .sheet{position:absolute;left:102px;top:81px;width:996px;height:615px;background:var(--paper);overflow:hidden}
  .header{position:absolute;left:0;top:0;width:996px;height:97px}
  .header svg{position:absolute;left:0;top:0}
  .header-photo{position:absolute;left:0;top:0;width:150px;height:97px;
    background:linear-gradient(90deg,rgba(160,170,165,.75) 0%,rgba(110,125,118,.5) 45%,rgba(40,51,33,0) 100%)}
  .headline{position:absolute;left:92px;top:13px;font-family:"Roboto Condensed",sans-serif;font-weight:800;font-size:54px;color:#fff;letter-spacing:-.5px;line-height:1;white-space:nowrap}
  .brand{position:absolute;left:656px;top:24px;display:flex;align-items:center;gap:12px}
  .brand-dot{width:50px;height:50px;border-radius:50%;background:var(--forest)}
  .brand-name{font-family:"Roboto",sans-serif;font-weight:700;font-size:38px;color:var(--forest);letter-spacing:1px}
  .lead{position:absolute;left:92px;top:117px;font-family:"Roboto Condensed",sans-serif;font-weight:700;font-size:29px;color:var(--forest);letter-spacing:-.2px;white-space:nowrap}
  .icon{position:absolute;width:48px;height:48px;border-radius:50%;background:var(--forest);display:flex;align-items:center;justify-content:center}
  .block-title{position:absolute;font-weight:500;font-size:22px;color:var(--forest);white-space:nowrap}
  .block-text{position:absolute;font-weight:300;font-size:13.5px;line-height:18.2px;color:var(--ink)}
  .benefits{position:absolute;left:159px;top:367px;list-style:none}
  .benefits li{position:relative;padding-left:20px;font-weight:300;font-size:13.5px;height:24px;line-height:18px;color:var(--ink);white-space:nowrap}
  .benefits svg{position:absolute;left:0;top:5px}
  .quote{position:absolute;left:584px;top:366px;font-style:italic;font-weight:500;font-size:14.5px;line-height:19.5px;color:var(--forest);width:330px}
  .quote-mark{position:absolute;font-family:"Roboto Condensed",sans-serif;font-weight:800;font-size:44px;color:var(--lime);line-height:1}
  .stars{position:absolute;left:584px;top:429px;display:flex;gap:5px}
  .footer-band{position:absolute;left:0;top:520px;width:996px;height:95px;background:var(--forest)}
  .cta{position:absolute;left:0;width:996px;text-align:center;color:#fff;font-size:23px;font-weight:300;top:548px;white-space:nowrap}
  .cta strong{font-weight:700}
  .contact{position:absolute;left:0;width:996px;text-align:center;color:var(--lime);font-size:23px;font-weight:700;top:576px;white-space:nowrap}
</style>
</head>
<body>
<div class="sheet">
  <header class="header">
    <svg width="996" height="97" viewBox="0 0 996 97">
      <polygon points="0,0 634,0 590,97 0,97" fill="var(--forest)"/>
      <polygon points="644,0 996,0 996,97 600,97" fill="var(--lime)"/>
    </svg>
    <div class="header-photo" role="img" aria-label="Foto: Hände mit Stift über Dokumenten und Diagrammen am Arbeitsplatz"></div>
    <h1 class="headline">Was wäre, wenn...</h1>
    <div class="brand"><span class="brand-dot"></span><span class="brand-name">Kalvor</span></div>
  </header>

  <h2 class="lead">...Sie neue Standorte mit echten Transportkosten vergleichen könnten?</h2>

  <div class="icon" style="left:96px;top:175px">
    <svg width="28" height="28" viewBox="0 0 28 28" fill="none" stroke="#fff" stroke-width="1.3"><circle cx="13" cy="15" r="11"/><circle cx="13" cy="15" r="7"/><circle cx="13" cy="15" r="3"/><path d="M13 15 L25 3 M21 3h4v4"/></svg>
  </div>
  <h3 class="block-title" style="left:159px;top:184px">Ausgangslage &amp; Ziel</h3>
  <p class="block-text" style="left:159px;top:220px;width:258px">Ein Handelsunternehmen prüfte mehrere neue Standorte. Dabei ging es um die Frage: Wie verändern sich die Transportkosten und die Kundenbelieferung bei einem Umzug?</p>

  <div class="icon" style="left:512px;top:175px">
    <svg width="28" height="28" viewBox="0 0 28 28" fill="none" stroke="#fff" stroke-width="1.3"><circle cx="15" cy="9" r="5"/><path d="M13 14v3h4v-3M15 1v1M9 3l1 1M21 3l-1 1"/><path d="M2 20h4v6H2zM6 21c4-2 7-2 10 0h4c2 0 2 2 0 2h-6M6 25h10l8-5c1-1 0-3-2-2l-4 2"/></svg>
  </div>
  <h3 class="block-title" style="left:584px;top:184px">Die Lösung – Unsere Simulation</h3>
  <p class="block-text" style="left:584px;top:220px;width:322px">Wir kombinierten Standortdaten, Kundenadressen und Liefermengen mit einem automatisierten Tourenplaner. So wurden die neuen Transportkosten und Fahrzeiten für alle Varianten berechnet und visualisiert.</p>

  <div class="icon" style="left:96px;top:322px">
    <svg width="30" height="30" viewBox="0 0 30 30" fill="none" stroke="#fff" stroke-width="1.3"><rect x="2" y="8" width="26" height="19" rx="2"/><circle cx="15" cy="7" r="4"/><path d="M7 26v-5M11 26v-8M19 26v-9M23 26v-12"/><circle cx="7" cy="15" r="2"/></svg>
  </div>
  <h3 class="block-title" style="left:159px;top:331px">Der konkrete Nutzen</h3>
  <ul class="benefits">
    <li><svg width="12" height="10" viewBox="0 0 12 10"><path d="M1 5l3.5 4L11 1" fill="none" stroke="var(--forest)" stroke-width="1.5"/></svg>Vergleich der Standorte mit echten Touren</li>
    <li><svg width="12" height="10" viewBox="0 0 12 10"><path d="M1 5l3.5 4L11 1" fill="none" stroke="var(--forest)" stroke-width="1.5"/></svg>Transparente Berechnung der Transportkosten</li>
    <li><svg width="12" height="10" viewBox="0 0 12 10"><path d="M1 5l3.5 4L11 1" fill="none" stroke="var(--forest)" stroke-width="1.5"/></svg>Klare Entscheidungsgrundlage für Geschäftsleitung</li>
    <li><svg width="12" height="10" viewBox="0 0 12 10"><path d="M1 5l3.5 4L11 1" fill="none" stroke="var(--forest)" stroke-width="1.5"/></svg>Erste Resultate in weniger als 3 Wochen</li>
  </ul>

  <div class="icon" style="left:512px;top:322px">
    <svg width="28" height="28" viewBox="0 0 28 28" fill="none" stroke="#fff" stroke-width="1.3"><path d="M3 5h18v14H10l-5 4v-4H3z"/><path d="M7 10h8M7 14h6M17 14l8-8 2 2-8 8h-2z"/></svg>
  </div>
  <h3 class="block-title" style="left:584px;top:331px">Kundenfeedback</h3>
  <span class="quote-mark" style="left:558px;top:362px">“</span>
  <p class="quote">Wir wussten genau, welcher Standort für unsere Kundenbelieferung am effizientesten ist – datenbasiert und nachvollziehbar.</p>
  <span class="quote-mark" style="left:802px;top:404px">”</span>
  <div class="stars">
    <svg width="90" height="14" viewBox="0 0 90 14" fill="var(--lime)">
      <path id="star" d="M7 0l1.8 4.6 4.9.3-3.8 3.1 1.2 4.8L7 10.2 2.9 12.8l1.2-4.8L.3 4.9l4.9-.3z"/>
      <use href="#star" x="19"/><use href="#star" x="38"/><use href="#star" x="57"/><use href="#star" x="76"/>
    </svg>
  </div>

  <div class="footer-band" role="img" aria-label="Dekorative Fläche: ansteigende Diagrammsilhouette im Fussbereich"></div>

  <p class="cta"><strong>Jetzt testen:</strong> Standortentscheidung absichern mit Simulation</p>
  <p class="contact">+41 44 000 12 34 &nbsp;I&nbsp; info@kalvor.ch</p>
</div>
</body>
</html>
```